PowerPoint template for Law Firm

We Need a PowerPoint Template for a Law Firm in Switzerland. We are primarly consult in business law. We Need a template for PowerPoint to Show Information to our Clients (inheritence law, corporate law, legal structures etc.) The design should be contemporary, simple and clear. It should be in harmony with our website: www.tannquist.com Style: professional, structured and clearly arranged. Colors: Blue (R: 1, G: 61: B: 105), white. Font: Calibri Ratio: 16: 9 Esamples attached

```html
<!DOCTYPE html>
<html lang="en">
<head>
<meta charset="utf-8">
<title>Tannquist Lawyers – Presentation Template</title>
<link rel="stylesheet" href="https://fonts.googleapis.com/css2?family=Carlito:wght@400;700&family=Roboto:wght@400;500;700&display=swap">
<style>
  :root {
    --stage: #ec2479;
    --navy: #1a406f;
    --white: #ffffff;
    --sky: #3f8fd0;
    --pale-sky: #b9dcf3;
    --teal-title: #3ca6d6;
    --mist: #ececec;
    --slate: #555a60;
    --soft-text: #dfe6ee;
  }
  html, body {
    margin: 0;
    width: 1200px;
    height: 849px;
    overflow: hidden;
    background: var(--stage);
  }
  .board { position: relative; width: 1200px; height: 849px; }
  .slide { position: absolute; display: block; overflow: hidden; }
  .slide svg { display: block; width: 100%; height: 100%; }
  .slide--cover { left: 291px; top: 15px; width: 554px; height: 336px; }
  .slide--services { left: 43px; top: 373px; width: 341px; height: 206px; }
  .slide--contact { left: 412px; top: 373px; width: 341px; height: 206px; }
  .slide--what { left: 775px; top: 373px; width: 341px; height: 206px; }
  .slide--content { left: 43px; top: 607px; width: 341px; height: 206px; }
  .slide--about { left: 409px; top: 607px; width: 341px; height: 206px; }
  .slide--team { left: 770px; top: 607px; width: 340px; height: 206px; }

  .brand { font-family: 'Carlito', 'Calibri', sans-serif; font-weight: 400; font-size: 24px; fill: var(--white); }
  .cover-title { font-family: 'Roboto', sans-serif; font-weight: 700; font-size: 38px; fill: var(--white); letter-spacing: 0.5px; }
  .cover-lead { font-family: 'Carlito', 'Calibri', sans-serif; font-size: 15px; fill: var(--soft-text); letter-spacing: 0.3px; }
  .heading { font-family: 'Roboto', sans-serif; font-weight: 500; }
  .body-line { font-family: 'Roboto', sans-serif; font-size: 7.5px; }
  .navy-fill { fill: var(--navy); }
  .white-fill { fill: var(--white); }
</style>
</head>
<body>
<main class="board">

  <!-- Cover slide -->
  <section class="slide slide--cover">
    <svg viewBox="0 0 810 492" aria-label="Cover slide">
      <rect width="810" height="492" fill="var(--navy)"/>
      <circle cx="729" cy="73" r="105" fill="var(--white)"/>
      <circle cx="44" cy="458" r="73" fill="none" stroke="#f2f2f2" stroke-width="45"/>
      <rect x="179" y="178" width="430" height="46" rx="23" fill="#2c5283" role="img" aria-label="Line drawing of the Swiss Alps skyline"/>
      <text class="brand" x="21" y="48">Tannquist-lawyers</text>
      <text class="cover-title" x="410" y="321" text-anchor="middle">HEAD TEXT HERE</text>
      <text class="cover-lead" x="410" y="351" text-anchor="middle">Lorem Ipsum is simply dummy text of the printing and typeset-</text>
      <text class="cover-lead" x="410" y="371" text-anchor="middle">ting industry. Lorem Ipsum has been the industry's standard</text>
      <text class="cover-lead" x="410" y="391" text-anchor="middle">dummy text ever since the 1500s,</text>
    </svg>
  </section>

  <!-- Our services -->
  <section class="slide slide--services">
    <svg viewBox="0 0 498 301" aria-label="Our services slide">
      <defs>
        <linearGradient id="photo-services" x1="0" y1="0" x2="0" y2="1">
          <stop offset="0" stop-color="#a9d3cc"/><stop offset="0.6" stop-color="#c9d6d2"/><stop offset="1" stop-color="#5c6670"/>
        </linearGradient>
      </defs>
      <rect width="498" height="301" fill="var(--white)"/>
      <circle cx="325" cy="-32" r="70" class="navy-fill"/>
      <circle cx="497" cy="152" r="42" class="navy-fill"/>
      <circle cx="312" cy="259" r="22" fill="none" stroke="var(--navy)" stroke-width="7"/>
      <circle cx="37" cy="150" r="193" class="navy-fill"/>
      <circle cx="37" cy="150" r="168" fill="url(#photo-services)" role="img" aria-label="Photo of a lawyer writing notes beside a laptop"/>
      <text class="heading" x="249" y="121" font-size="15" fill="var(--navy)">OUR SERVICES</text>
      <text class="body-line" x="249" y="138" fill="var(--navy)">Lorem Ipsum is simply dummy text of the</text>
      <text class="body-line" x="249" y="152" fill="var(--navy)">Lorem Ipsum is simply dummy text of the</text>
      <text class="body-line" x="249" y="166" fill="var(--navy)">Lorem Ipsum is simply dummy text of the</text>
      <text class="body-line" x="249" y="180" fill="var(--navy)">Lorem Ipsum is simply dummy text of the</text>
    </svg>
  </section>

  <!-- Contact -->
  <section class="slide slide--contact">
    <svg viewBox="0 0 498 301" aria-label="Contact slide">
      <rect width="498" height="301" fill="var(--white)"/>
      <circle cx="323" cy="-15" r="70" fill="var(--mist)"/>
      <circle cx="548" cy="152" r="185" class="navy-fill"/>
      <circle cx="16" cy="155" r="50" fill="none" stroke="var(--pale-sky)" stroke-width="4"/>
      <circle cx="64" cy="133" r="58" class="navy-fill"/>
      <circle cx="284" cy="279" r="23" fill="none" stroke="var(--pale-sky)" stroke-width="7"/>
      <text class="heading" x="150" y="113" font-size="16" fill="var(--slate)">CONTATC US</text>
      <text class="body-line" x="152" y="137" font-size="8" fill="#222">Lorem Ipsum is simply dummy text of the</text>
      <text class="body-line" x="152" y="154" font-size="8" fill="#222">Lorem Ipsum is simply dummy text of the</text>
      <text class="body-line" x="152" y="171" font-size="8" fill="#222">Lorem Ipsum is simply dummy text of the</text>
      <text class="body-line" x="152" y="188" font-size="8" fill="#222">Lorem Ipsum is simply dummy text of the</text>
    </svg>
  </section>

  <!-- What we do -->
  <section class="slide slide--what">
    <svg viewBox="0 0 498 301" aria-label="What we do slide">
      <defs>
        <linearGradient id="photo-what" x1="0" y1="0" x2="0" y2="1">
          <stop offset="0" stop-color="#a9d3cc"/><stop offset="0.55" stop-color="#c9d6d2"/><stop offset="1" stop-color="#5c6670"/>
        </linearGradient>
      </defs>
      <rect width="498" height="301" fill="var(--navy)"/>
      <circle cx="74" cy="3" r="37" fill="none" stroke="var(--white)" stroke-width="10"/>
      <circle cx="272" cy="157" r="85" fill="var(--sky)"/>
      <circle cx="370" cy="153" r="120" class="white-fill"/>
      <circle cx="370" cy="153" r="111" class="navy-fill"/>
      <circle cx="370" cy="153" r="103" fill="url(#photo-what)" role="img" aria-label="Photo of a lawyer writing notes beside a laptop"/>
      <text class="heading" x="63" y="95" font-size="18" fill="var(--teal-title)">WHAT WE DO</text>
      <g class="body-line" font-size="7" fill="var(--white)">
        <circle cx="52" cy="136" r="7" class="white-fill"/>
        <text x="67" y="133">Lorem Ipsum is simply dummy text of the</text>
        <text x="67" y="142">printing and typesetting industry.</text>
        <circle cx="52" cy="171" r="7" class="white-fill"/>
        <text x="67" y="168">Lorem Ipsum is simply dummy text of the</text>
        <text x="67" y="177">printing and typesetting industry.</text>
        <circle cx="52" cy="203" r="7" class="white-fill"/>
        <text x="67" y="200">Lorem Ipsum is simply dummy text of the</text>
        <text x="67" y="209">printing and typesetting industry.</text>
        <circle cx="52" cy="238" r="7" class="white-fill"/>
        <text x="67" y="235">Lorem Ipsum is simply dummy text of the</text>
        <text x="67" y="244">printing and typesetting industry.</text>
      </g>
    </svg>
  </section>

  <!-- Content -->
  <section class="slide slide--content">
    <svg viewBox="0 0 498 301" aria-label="Content slide">
      <rect width="498" height="301" fill="var(--navy)"/>
      <circle cx="492" cy="3" r="107" class="white-fill"/>
      <circle cx="22" cy="273" r="65" class="white-fill"/>
      <circle cx="22" cy="273" r="52" fill="#e8e8e8" stroke="var(--navy)" stroke-width="3"/>
      <text class="heading" x="90" y="121" font-size="19" fill="var(--white)">CONTENT</text>
      <g class="body-line" font-size="7" fill="var(--white)">
        <circle cx="92" cy="158" r="7" class="white-fill"/>
        <text x="107" y="155">Lorem Ipsum is simply dummy text of the</text>
        <text x="107" y="164">printing and typesetting industry.</text>
        <circle cx="278" cy="158" r="7" class="white-fill"/>
        <text x="293" y="155">Lorem Ipsum is simply dummy text of the</text>
        <text x="293" y="164">printing and typesetting industry.</text>
        <circle cx="92" cy="193" r="7" class="white-fill"/>
        <text x="107" y="190">Lorem Ipsum is simply dummy text of the</text>
        <text x="107" y="199">printing and typesetting industry.</text>
        <circle cx="278" cy="193" r="7" class="white-fill"/>
        <text x="293" y="190">Lorem Ipsum is simply dummy text of the</text>
        <text x="293" y="199">printing and typesetting industry.</text>
      </g>
    </svg>
  </section>

  <!-- About us -->
  <section class="slide slide--about">
    <svg viewBox="0 0 498 301" aria-label="About us slide">
      <defs>
        <linearGradient id="photo-about" x1="0" y1="0" x2="0" y2="1">
          <stop offset="0" stop-color="#a9d3cc"/><stop offset="0.55" stop-color="#c9d6d2"/><stop offset="1" stop-color="#5c6670"/>
        </linearGradient>
      </defs>
      <rect width="498" height="301" fill="var(--white)"/>
      <circle cx="158" cy="6" r="45" fill="none" stroke="var(--navy)" stroke-width="13"/>
      <circle cx="0" cy="273" r="52" class="navy-fill"/>
      <circle cx="397" cy="153" r="125" class="navy-fill"/>
      <circle cx="397" cy="153" r="112" class="white-fill"/>
      <circle cx="397" cy="153" r="105" fill="url(#photo-about)" role="img" aria-label="Photo of a lawyer writing notes beside a laptop"/>
      <text class="heading" x="45" y="125" font-size="19" fill="var(--navy)">ABOUT US</text>
      <g class="body-line" font-size="7.5" fill="var(--navy)">
        <text x="45" y="149">Lorem ipsum dolor sit amet, consectetuer adipiscing</text>
        <text x="45" y="159">elit, sed diam nonummy nibh euismod tincidunt ut</text>
        <text x="45" y="169">laoreet dolore magna aliquam erat volutpat. Ut wisi</text>
        <text x="45" y="180">enim ad minim veniam, quis nostrud exerci tation</text>
        <text x="45" y="190">ullamcorper suscipit lobortis nisl ut aliquip ex ea com</text>
      </g>
    </svg>
  </section>

  <!-- Our team -->
  <section class="slide slide--team">
    <svg viewBox="0 0 498 301" aria-label="Our team slide">
      <defs>
        <linearGradient id="photo-team" x1="0" y1="0" x2="0" y2="1">
          <stop offset="0" stop-color="#a9d3cc"/><stop offset="0.55" stop-color="#c9d6d2"/><stop offset="1" stop-color="#5c6670"/>
        </linearGradient>
      </defs>
      <rect width="498" height="301" fill="var(--white)"/>
      <circle cx="324" cy="-12" r="72" fill="var(--sky)"/>
      <circle cx="564" cy="143" r="120" fill="none" stroke="var(--navy)" stroke-width="10"/>
      <circle cx="132" cy="143" r="90" fill="url(#photo-team)" role="img" aria-label="Photo of a lawyer writing notes beside a laptop"/>
      <circle cx="310" cy="260" r="23" fill="none" stroke="var(--navy)" stroke-width="8"/>
      <circle cx="42" cy="323" r="45" class="navy-fill"/>
      <text class="heading" x="248" y="107" font-size="19" fill="var(--navy)">OUR TEAM</text>
      <text class="body-line" x="250" y="134" fill="var(--navy)">Lorem Ipsum is simply dummy text of the</text>
      <text class="body-line" x="250" y="148" fill="var(--navy)">Lorem Ipsum is simply dummy text of the</text>
      <text class="body-line" x="250" y="162" fill="var(--navy)">Lorem Ipsum is simply dummy text of the</text>
      <text class="body-line" x="250" y="176" fill="var(--navy)">Lorem Ipsum is simply dummy text of the</text>
    </svg>
  </section>

</main>
</body>
</html>
```